CodeVarnaly.com Redesign

Please read the notes and see the site-map attached.
Updates

We are looking for something highly creative. Please provide your best work. Best of luck and thank you very much for your hard work!

Reason: I am seeing good designs but I am not seeing great designs. I really need a design that is unique and is going to wow me. No one is required to stick to the existing color schemes etc. You are free to use other colors etc. I am seeing a lot of the same colors that are used on the site now.

Target Market(s)

Business and entrepreneurs mainly. People looking to build applications, software or launch web or mobile tech products.

Colors

Designer to choose colors to be used in the design.

Requirements
Must have
• See my attached html file.
Nice to have
Should not have
• No sure

```html
<!DOCTYPE html>
<html lang="en">
<head>
<meta charset="utf-8">
<title>CodeVarnaly — Your Development Partner</title>
<link href="https://fonts.googleapis.com/css2?family=Open+Sans:wght@400;600;700;800&display=swap" rel="stylesheet">
<style>
:root{
  --navy:#1b4a5e;
  --navy-deep:#0f2f3d;
  --navy-item:#2e5a6b;
  --green:#7cc142;
  --green-dark:#5fa032;
  --text:#1b4a5e;
  --muted:#8a8a8a;
  --light:#ececec;
  --black:#232323;
  --white:#ffffff;
}
*{margin:0;padding:0;box-sizing:border-box}
html,body{width:764px;height:1200px;overflow:hidden}
body{font-family:"Open Sans",Arial,sans-serif;color:var(--text);background:var(--white);position:relative}
section,header,footer{position:absolute;left:0;width:764px}
.abs{position:absolute}

/* header */
.site-header{top:0;height:58px;background:var(--white);border-bottom:1px solid #ddd}
.brand{left:110px;top:20px;display:flex;align-items:center;gap:6px;font-size:20px;font-weight:600;color:var(--green)}
.brand-dot{width:22px;height:22px;border-radius:50%;background:var(--navy)}
.contact-top{left:470px;top:13px;width:101px;font-size:7px;text-align:right;line-height:11px;color:var(--navy)}
.contact-top svg{vertical-align:-1px;margin-right:2px}
.login{left:580px;top:12px;width:75px;height:19px;border:1px solid #bbb;border-radius:2px;font-size:7px;color:#777;display:flex;align-items:center;justify-content:center;gap:3px}
.main-nav{top:40px;left:331px;display:flex;font-size:8px;font-weight:600}
.main-nav a{color:var(--navy);text-decoration:none;margin-right:20px}
.main-nav a:last-child{margin-right:0}
.main-nav a.active{color:var(--green)}

/* hero */
.hero{top:58px;height:276px;background:linear-gradient(90deg,#8c8c8c 0%,#b3b3b3 45%,#c4c4c4 100%)}
.hero-photo{left:400px;top:0;width:300px;height:276px;background:radial-gradient(circle at 50% 45%,#6a86a6 0%,#9aa8b8 45%,rgba(180,180,180,0) 75%)}
.dots{left:110px;top:50px;display:flex;gap:3px}
.dots span{width:7px;height:7px;background:#ddd}
.dots span.on{background:var(--green)}
.hero h1{left:110px;top:74px;width:260px;font-size:20px;line-height:25px;font-weight:700;color:var(--white);text-transform:uppercase}
.hero-lead{left:110px;top:130px;width:260px;font-size:7.4px;line-height:9px;color:var(--white);font-weight:600}
.hero-tag{left:110px;top:172px;font-size:7.4px;font-weight:700;color:var(--white)}
.btn{height:22px;font-size:8.5px;font-weight:600;display:flex;align-items:center;justify-content:center;gap:4px;border-radius:2px}
.btn-services{left:110px;top:203px;width:98px;background:var(--white);border:2px solid var(--green);color:var(--green-dark)}
.btn-quote{left:212px;top:203px;width:94px;border:1px solid #666;color:var(--navy)}
.hire-tab{left:652px;top:125px;width:112px;height:30px;background:var(--white);border-radius:4px 0 0 4px;border:2px solid #d4e9c4;border-right:0;padding:5px 0 0 32px;font-size:8px;font-weight:700;line-height:8px;color:var(--navy)}
.hire-tab small{display:block;font-size:6px;color:var(--green);font-weight:600}
.hire-tab i{position:absolute;left:7px;top:5px;width:18px;height:16px;border:2px solid var(--navy);border-radius:2px}

/* cases & testimonials */
.split{top:334px;height:280px}
.cases{left:0;top:0;width:382px;height:280px;background:var(--navy)}
.love{left:382px;top:0;width:382px;height:280px;background:var(--green)}
.block-title{font-size:12px;font-weight:700;color:var(--white);text-transform:uppercase;display:flex;align-items:flex-end;gap:6px}
.cases .block-title{left:130px;top:21px}
.love .block-title{left:20px;top:21px}
.rule{height:1px;background:rgba(255,255,255,.3)}
.case{left:128px;width:234px;padding:9px 12px;color:var(--white);background:var(--navy-item)}
.case h3{font-size:10px;font-weight:600;margin-bottom:4px}
.case b{display:block;font-size:7px}
.case p{font-size:7px;line-height:8px}
.case.first{background:var(--navy-deep)}
.view-all{font-size:8px;font-weight:700;color:var(--white)}
.quote-text{left:20px;width:234px;font-size:7px;line-height:8.5px;color:var(--white)}
.quote-by{left:20px;font-size:7px;font-weight:700;color:var(--white)}

/* services */
.services{top:614px;height:189px;background:var(--white)}
.service{top:0;width:136px;text-align:center}
.service .icon{width:56px;height:56px;border-radius:50%;background:#8a8a8a;margin:51px auto 0}
.service h4{font-size:8.5px;font-weight:700;color:var(--muted);margin-top:11px;line-height:10px}
.service.featured{top:12px;height:167px;box-shadow:0 0 6px rgba(0,0,0,.2)}
.service.featured .icon{background:#f05a28;margin-top:39px}
.service.featured h4{color:var(--navy)}

/* quote form */
.quote{top:803px;height:159px;background:var(--light)}
.quote h2{left:0;width:764px;top:23px;text-align:center;font-size:12px;font-weight:700;color:var(--navy)}
.quote .rule{left:110px;top:46px;width:544px;background:#ddd}
.field{background:#f8f8f8;border:1px solid #ddd;font-size:8px;color:#aaa;padding:8px 12px}
.send{left:472px;top:72px;width:171px;height:60px;background:linear-gradient(#7cc142,#5fa032);color:var(--white);text-align:center;padding-top:18px;font-size:12px;font-weight:700;line-height:12px;border-radius:2px}
.send small{display:block;font-size:7px;font-weight:400}

/* follow */
.follow{top:962px;height:78px;background:var(--black)}
.follow-label{left:228px;top:32px;font-size:13px;font-weight:700;color:var(--white)}
.social{top:25px;width:32px;height:32px;display:flex;align-items:center;justify-content:center;font-size:6.5px;font-weight:600;color:var(--white)}

/* footer */
.site-footer{top:1040px;height:160px;background:var(--navy)}
.foot-nav{left:122px;top:18px;list-style:none;font-size:8px;line-height:17.6px;color:#9fd4ea}
.foot-nav li::before{content:"";display:inline-block;border-left:4px solid var(--white);border-top:3px solid transparent;border-bottom:3px solid transparent;margin-right:6px}
.foot-nav li:first-child{color:var(--white);font-weight:700}
.foot-contact{left:284px;top:21px;font-size:6.5px;line-height:10px;color:var(--white)}
.foot-contact h5{font-size:8px;font-weight:700}
.foot-contact .addr{color:#9fd4ea;line-height:8px;margin:1px 0 4px 12px}
.foot-brand{left:480px;top:52px;font-size:20px;font-weight:600;color:var(--white);display:flex;align-items:center;gap:6px}
.foot-copy{left:480px;top:76px;font-size:7.5px;line-height:10px;color:#4fb0d8}
</style>
</head>
<body>

<header class="site-header">
  <div class="abs brand"><span class="brand-dot"></span>codevarnaly</div>
  <div class="abs contact-top">
    <div><svg width="7" height="7" viewBox="0 0 10 10"><path d="M2 1l2 2-1 1.5a6 6 0 0 0 2.5 2.5L7 6l2 2-1.5 1.5C4 9 1 6 .5 2z" fill="#7cc142"/></svg>+1 (555) 014-2280</div>
    <div><svg width="8" height="6" viewBox="0 0 10 7"><rect x=".5" y=".5" width="9" height="6" fill="none" stroke="#7cc142"/><path d="M.5.5l4.5 3.5L9.5.5" fill="none" stroke="#7cc142"/></svg>reachus@codevarnaly.com</div>
  </div>
  <div class="abs login"><svg width="7" height="7" viewBox="0 0 10 10"><circle cx="5" cy="3" r="2.3" fill="#999"/><path d="M1 10a4 4 0 0 1 8 0z" fill="#999"/></svg>LOGIN</div>
  <nav class="abs main-nav">
    <a class="active">Home</a><a>Who We Are</a><a>What We Do</a><a>Case Studies</a><a>Blog</a><a>Reach Us</a>
  </nav>
</header>

<section class="hero">
  <div class="abs hero-photo" role="img" aria-label="Overhead photo of a team in business clothes joining hands in a circle"></div>
  <div class="abs dots"><span></span><span></span><span class="on"></span><span></span><span></span></div>
  <h1 class="abs">Your Development Partner</h1>
  <p class="abs hero-lead">We develop creative websites, web applications, mobile apps and custom applications that elicit smiles, create surprise and deliver more than expected.</p>
  <p class="abs hero-tag">From vision to production. CodeVarnaly can help.</p>
  <div class="abs btn btn-services"><svg width="9" height="9" viewBox="0 0 10 10"><circle cx="5" cy="5" r="3.2" fill="none" stroke="#5fa032" stroke-width="2.2" stroke-dasharray="1.6 1"/></svg>Our Services</div>
  <div class="abs btn btn-quote"><svg width="11" height="9" viewBox="0 0 12 10"><rect x="0" y="0" width="8" height="6" rx="2" fill="#1b4a5e"/><rect x="4" y="3" width="8" height="6" rx="2" fill="#1b4a5e"/></svg>Get a Quote</div>
  <div class="abs hire-tab"><i></i>HIRE US NOW<small>GET A QUOTE</small></div>
</section>

<section class="split">
  <div class="abs cases">
    <div class="abs block-title"><svg width="26" height="22" viewBox="0 0 26 22"><rect x="0" y="2" width="7" height="20" fill="#fff"/><rect x="9" y="0" width="7" height="22" fill="#fff"/><rect x="18" y="3" width="7" height="19" fill="#fff"/></svg>Case Studies</div>
    <div class="abs rule" style="left:128px;top:48px;width:234px"></div>
    <div class="abs case first" style="top:61px;height:53px">
      <h3>Client:</h3><b>Nova Reel</b><p>User Experience Design, Product Development</p>
      <svg class="abs" style="left:192px;top:10px" width="30" height="30" viewBox="0 0 30 30"><circle cx="12" cy="12" r="10" fill="none" stroke="#fff" stroke-width="2"/><path d="M12 7v10M7 12h10M19.5 19.5L28 28" stroke="#fff" stroke-width="2.4"/></svg>
    </div>
    <div class="abs case" style="top:117px;height:53px"><h3>Client:</h3><b>Learnloft Inc</b><p>Phonix, Tabora, Droidex, User Experience Design, Product Development</p></div>
    <div class="abs case" style="top:173px;height:54px"><h3>Client:</h3><b>Hartwell Quinn Company &amp; Brightway Media</b><p>Web Development, LAMP Development, PHP, Quarrydb, Modula, HTML5</p></div>
    <div class="abs rule" style="left:128px;top:231px;width:234px"></div>
    <div class="abs view-all" style="left:128px;top:250px">VIEW ALL CASES &gt;&gt;</div>
  </div>
  <div class="abs love">
    <div class="abs block-title"><svg width="28" height="22" viewBox="0 0 28 22"><path d="M0 22V11Q0 2 10 0v4q-5 1-5 7h5v11zM15 22V11q0-9 10-11v4q-5 1-5 7h5v11z" fill="#fff"/></svg>Why Clients Love Us!</div>
    <div class="abs rule" style="left:20px;top:48px;width:234px"></div>
    <p class="abs quote-text" style="top:60px">Using new vendors is always nerve-wracking for an organization, but boy are we pleased with the decision to switch to CodeVarnaly. They completed our project on-time, on-budget and even made suggestions to our web-site's back-end that has made the site's coordination and implementation of change much easier going forward. They came through 100% plus percent for us and we would definitely use them again without hesitation.</p>
    <div class="abs quote-by" style="top:131px">Dan Mercer, Managing Director-Stonebridge Capital LLC</div>
    <div class="abs rule" style="left:20px;top:150px;width:234px"></div>
    <p class="abs quote-text" style="top:163px">The CodeVarnaly team were great to work with. They were very professional and hit every deadline that I gave them without going over budget. I will continue to use their services and recommend it to friends.</p>
    <div class="abs quote-by" style="top:209px">Owen Hale, CEO-Northgate Seed Partners LLC</div>
    <div class="abs rule" style="left:20px;top:231px;width:234px"></div>
    <div class="abs view-all" style="left:20px;top:250px">VIEW ALL &gt;&gt;</div>
  </div>
</section>

<section class="services">
  <div class="abs service" style="left:110px"><div class="icon" role="img" aria-label="Illustration of a desktop monitor showing a website"></div><h4>Web<br>Development</h4></div>
  <div class="abs service" style="left:246px"><div class="icon" role="img" aria-label="Illustration of a smartphone with app icons"></div><h4>Mobile App<br>Development</h4></div>
  <div class="abs service featured" style="left:383px"><div class="icon" role="img" aria-label="Illustration of a monitor showing custom software"></div><h4>Custom Software<br>Development</h4></div>
  <div class="abs service" style="left:518px"><div class="icon" role="img" aria-label="Illustration of a monitor showing an interface layout"></div><h4>User Experience<br>Design</h4></div>
</section>

<section class="quote">
  <h2 class="abs"><svg width="24" height="20" viewBox="0 0 24 20" style="vertical-align:-4px;margin-right:4px"><rect x="0" y="0" width="16" height="11" rx="4" fill="#1b4a5e"/><path d="M3 10l-1 5 5-4z" fill="#1b4a5e"/><rect x="8" y="7" width="16" height="10" rx="4" fill="#1b4a5e" stroke="#ececec" stroke-width="1.5"/></svg>GET A QUOTE</h2>
  <div class="abs rule"></div>
  <div class="abs field" style="left:122px;top:72px;width:171px;height:28px">Name*</div>
  <div class="abs field" style="left:122px;top:104px;width:171px;height:28px">E-mail*</div>
  <div class="abs field" style="left:297px;top:72px;width:171px;height:60px">Message</div>
  <div class="abs send">SEND &gt;&gt;<small>Get a Quote Now !</small></div>
</section>

<section class="follow">
  <div class="abs follow-label">Follow us :</div>
  <div class="abs social" style="left:310px;background:#c6303a">Circlo</div>
  <div class="abs social" style="left:347px;background:#b7312c">Vidora</div>
  <div class="abs social" style="left:385px;background:#3b5a96">Kinly</div>
  <div class="abs social" style="left:423px;background:#1aa6d8">Chirpa</div>
  <div class="abs social" style="left:461px;background:#f29b1a">Feedy</div>
  <div class="abs social" style="left:499px;background:#1b78b4">Linkwell</div>
</section>

<footer class="site-footer">
  <ul class="abs foot-nav">
    <li>Home</li><li>Who We Are</li><li>What We Do</li><li>Case Studies</li><li>Blog</li><li>Reach Us</li><li>Privacy Policy</li>
  </ul>
  <div class="abs foot-contact">
    <h5><svg width="9" height="8" viewBox="0 0 10 9"><path d="M5 0l5 4.5H8.5V9h-7V4.5H0z" fill="#fff"/></svg> CodeVarnaly LLC</h5>
    <div class="addr">2210 Harbor Lane #40<br>Maple Ridge,<br>CA 90000</div>
    <div>Voice: +1 (555) 014-2280</div>
    <div>Email: reachus@codevarnaly.com</div>
    <div>Talkly: codevarnaly</div>
  </div>
  <div class="abs foot-brand"><span class="brand-dot" style="background:var(--white)"></span>codevarnaly</div>
  <div class="abs foot-copy">Copyright © 2014 CodeVarnaly LLC.<br>All Rights Reserved.</div>
</footer>

</body>
</html>
```